Security based company delivering High Risk Training to Law Enforcement Agencies Worldwide.

We need a Web design for a company doing business in Washington D.C. We deliver High Risk Training to Law Enforcement Agencies throughout the world. Our focus is on Improvised Explosive Devices. We train Bomb Technicians and First Responders in all aspects relating to bombings and criminal incidents globally.
Updates

Reason: We have uploaded our logo. Thank you.

Target Market(s)

Military and Law Enforcement Personnel from around the world.

Industry/Entity Type

Business

Requirements
Should not have
• Do not include cartoon like characters.

```html
<!DOCTYPE html>
<html lang="en">
<head>
<meta charset="utf-8">
<title>Korvant International</title>
<link rel="stylesheet" href="https://fonts.googleapis.com/css2?family=Roboto:wght@700&family=Mulish:wght@400&family=Open+Sans:wght@400&family=Roboto+Condensed:wght@400&display=swap">
<style>
:root{
  --black:#0b0b0b;
  --nav:#d8d8d8;
  --band:#eeeeee;
  --page:#f5f5f5;
  --ink:#333333;
  --muted:#777777;
  --red:#e0393b;
  --footer:#7b7b7b;
  --white:#ffffff;
}
*{box-sizing:border-box;margin:0;padding:0}
html,body{width:1063px;height:1200px;overflow:hidden}
body{position:relative;background:var(--page);font-family:"Open Sans",sans-serif;color:var(--ink)}
.abs{position:absolute}
.header{left:0;top:0;width:1063px;height:70px;background:linear-gradient(#111,#050505)}
.brand{left:76px;top:0;width:237px;height:81px;background:var(--black);border:1px solid #333;border-top:0;display:flex;align-items:center;justify-content:center;gap:10px;z-index:3}
.brand-mark{width:22px;height:22px;border-radius:50%;background:var(--red)}
.brand-name{font-family:"Mulish",sans-serif;font-size:17px;color:var(--white);letter-spacing:1px;line-height:1.1}
.nav{top:33px;left:365px;display:flex;gap:25px;font-family:"Mulish",sans-serif;font-size:12px;color:var(--nav)}
.search{left:786px;top:26px;width:201px;height:26px;border:1px solid #666;border-radius:3px}
.search svg{position:absolute;right:8px;top:6px}
.hero{left:0;top:70px;width:1063px;height:505px;background:linear-gradient(100deg,#3a3a3a 0%,#6f6f6f 30%,#9b9b9b 60%,#8a8a8a 85%,#5d5d5d 100%)}
.hero-title{left:0;top:280px;width:1063px;padding-left:150px;text-align:center;font-family:"Roboto",sans-serif;font-weight:700;color:var(--white);text-shadow:0 2px 4px rgba(0,0,0,.6);line-height:1}
.hero-title .l1{font-size:40px;display:block}
.hero-title .l2{font-size:45px;display:block;margin-top:13px}
.dots{left:490px;top:495px;display:flex;gap:11px}
.dots span{width:12px;height:12px;border-radius:50%;background:#444}
.dots span:first-child{background:var(--white)}
.services{left:0;top:575px;width:1063px;height:245px;background:var(--band);box-shadow:0 4px 8px rgba(0,0,0,.15)}
.card{top:32px;width:280px}
.card .photo{height:156px;border:8px solid #8a8a8a;outline:1px solid #ccc;outline-offset:-9px}
.card p{margin-top:14px;text-align:center;font-size:15px;color:#222}
.welcome-title{left:75px;top:862px;font-family:"Mulish",sans-serif;font-size:24px;color:var(--red)}
.welcome-photo{left:75px;top:910px;width:216px;height:157px;background:linear-gradient(120deg,#bdbdbd,#6a5a4a 55%,#d06a20 75%,#2a2a2a)}
.welcome-text{left:308px;top:907px;width:362px;font-size:12.4px;line-height:16.4px;color:#444}
.welcome-text p+p{margin-top:16px}
.divider{left:700px;top:870px;width:1px;height:230px;background:#e2e2e2}
.news-title{left:722px;top:862px;font-family:"Mulish",sans-serif;font-size:24px;color:var(--red)}
.news-next{left:961px;top:869px}
.news{left:722px;width:262px;display:flex;gap:11px}
.date{width:50px;height:53px;border:1px solid #ddd;background:var(--white);text-align:center}
.date b{display:block;font-weight:400;font-size:15px;line-height:35px;color:#333}
.date i{display:block;font-style:normal;font-size:10px;line-height:17px;background:#e6e6e6;color:#555}
.news h3{font-family:"Mulish",sans-serif;font-weight:400;font-size:13px;color:#222;margin-top:-2px}
.news p{font-size:11px;line-height:15px;color:var(--muted);margin-top:7px}
.news a{color:var(--red);text-decoration:none;font-size:10px;margin-left:4px}
.rule{left:722px;top:978px;width:261px;border-top:1px dotted #999}
.footer{left:0;top:1114px;width:1063px;height:86px;background:var(--footer);font-family:"Roboto Condensed",sans-serif;color:var(--white);font-size:10.5px}
.footer-links{left:78px;top:22px;word-spacing:2px}
.copyright{left:78px;top:47px}
.social{left:846px;top:26px;display:flex;gap:6px}
.social span{width:30px;height:30px;border-radius:50%;background:#5f5f5f}
</style>
</head>
<body>
<header class="abs header">
  <div class="abs brand"><span class="brand-mark"></span><span class="brand-name">KORVANT<br>INTERNATIONAL</span></div>
  <nav class="abs nav"><span>HOME</span><span>ABOUT US</span><span>SERVICES</span><span>TRAINING</span><span>CONTACT</span></nav>
  <div class="abs search"><svg width="12" height="12" viewBox="0 0 12 12"><circle cx="5" cy="5" r="3.8" fill="none" stroke="#777" stroke-width="1.6"/><line x1="8" y1="8" x2="11" y2="11" stroke="#777" stroke-width="2"/></svg></div>
</header>

<section class="abs hero" role="img" aria-label="Black and white photo of a bomb technician in a protective suit kneeling beside equipment near a stop sign"></section>
<h1 class="abs hero-title"><span class="l1">HIGH RISK TRAINING TO</span><span class="l2">LAW ENFORCEMENT AGENCIES</span></h1>
<div class="abs dots"><span></span><span></span><span></span><span></span></div>

<section class="abs services">
  <div class="abs card" style="left:75px"><div class="photo" role="img" aria-label="Yellow explosive block flying over a desert range" style="background:linear-gradient(#d8d0cc,#d9c0a4)"></div><p>BOMB TECHNICIANS</p></div>
  <div class="abs card" style="left:387px"><div class="photo" role="img" aria-label="Controlled blast throwing debris and dust in the desert" style="background:linear-gradient(#c9c6c2,#7d7264 50%,#c9b49a)"></div><p>BOMBINGS</p></div>
  <div class="abs card" style="left:708px"><div class="photo" role="img" aria-label="White car engulfed by an explosion fireball" style="background:linear-gradient(100deg,#c8c4bc,#dedad2 50%,#f0a040 80%,#c98a50)"></div><p>CRIMINAL INCIDENTS</p></div>
</section>

<h2 class="abs welcome-title" style="font-weight:400">Welcome to The Enforcement Specialist</h2>
<div class="abs welcome-photo" role="img" aria-label="Car burning with thick black smoke during an explosives demonstration"></div>
<div class="abs welcome-text">
  <p>Lorem ipsum dolor sit amet, consectetur adipisicing elit, sed do eiusmod tempor incididunt ut labore et dolore magna aliqua. Ut enim ad minim veniam, quis nostrud exercitation ullamco laboris nisi ut aliquip ex ea commodo consequat. Duis aute irure dolor in reprehenderit in voluptate velit esse cillum dolore eu fugiat nulla pariatur.</p>
  <p>Excepteur sint occaecat cupidatat non proident, sunt in culpa qui officia deserunt mollit anim id est laborum.Lorem ipsum dolor sit amet, consectetur adipisicing elit, sed do eiusmod tempor incididunt ut labore et dolore magna aliqua.</p>
</div>

<div class="abs divider"></div>
<h2 class="abs news-title" style="font-weight:400">Latest News</h2>
<svg class="abs news-next" width="18" height="18" viewBox="0 0 18 18"><circle cx="9" cy="9" r="8" fill="none" stroke="#222" stroke-width="1.3"/><path d="M7.5 5.5 11 9l-3.5 3.5" fill="none" stroke="#222" stroke-width="1.5"/></svg>

<article class="abs news" style="top:910px">
  <div class="date"><b>20</b><i>mar</i></div>
  <div><h3>News Headline Goes Here</h3><p>Lorem ipsum dolor sit amet, consectetur adipisicing elit <a href="#">Read More ...</a></p></div>
</article>
<div class="abs rule"></div>
<article class="abs news" style="top:1002px">
  <div class="date"><b>20</b><i>mar</i></div>
  <div><h3>News Headline Goes Here</h3><p>Lorem ipsum dolor sit amet, consectetur adipisicing elit <a href="#">Read More ...</a></p></div>
</article>

<footer class="abs footer">
  <div class="abs footer-links">ABOUT US &nbsp;|&nbsp; SERVICES &nbsp;|&nbsp; TRAINING &nbsp;|&nbsp; CONTACT &nbsp;|&nbsp; TERMS &amp; USE</div>
  <div class="abs copyright">ALL RIGHTS RESERVED. COPYRIGHTS @ 2014</div>
  <div class="abs social"><span></span><span></span><span></span><span></span></div>
</footer>
</body>
</html>
```